Trade Show Booth Sign Design for Retracting Banner

I need a trade show booth sign designed. It will be for a retractable banner that is double sided with 34 by 81 inch.

I want to incorporate my logo (see attached, have it in other file formats as well) and graphics from my website (https://www.pellacorvaadvisory.com/) with parts or all of the following text.

· Educational Content Creation
o Supplemental Textbook Content Development
o E-learning Content Development
· Curriculum Development
o VKTR/Joint Pillar
o Three Dimensional Learning
· Assessment
o Formative Assessments
o Elementary School, Middle School, High School, College, and Business
· Professional Development
o Training
o Facilitation

Target Market(s)

Education

Industry/Entity Type

Education

Font styles to use
Sans Serif

Colors

Designer to choose colors to be used in the design.

Requirements
Must have
• Eye catching and easy to read design
Nice to have
• Would like to see incorporation of my logo and some of the elements of my website images
Should not have
• N/A

```html
<!DOCTYPE html>
<html lang="en">
<head>
<meta charset="utf-8">
<title>Pellacorva Advisory – Retractable Banner</title>
<link href="https://fonts.googleapis.com/css2?family=Fira+Sans+Extra+Condensed:wght@400;600;700;800&display=swap" rel="stylesheet">
<style>
  :root {
    --navy: #0d2a63;
    --gold: #edb12a;
    --yellow: #f8d42a;
    --teal-dark: #1b8a93;
    --teal-light: #8fd8d6;
    --paper-top: #f7f7f7;
    --paper-bottom: #dcdcdc;
    --stage: #e6e6e6;
  }
  html, body {
    margin: 0;
    width: 1200px;
    height: 1200px;
    overflow: hidden;
    background: var(--stage);
  }
  .canvas {
    width: 1200px;
    height: 1200px;
    display: flex;
    align-items: center;
    justify-content: center;
  }
  .banner {
    width: 465px;
    height: 1155px;
    display: block;
    font-family: "Fira Sans Extra Condensed", "Arial Narrow", sans-serif;
  }
  .brand-name { fill: var(--navy); font-weight: 800; }
  .service-title { fill: var(--navy); font-weight: 700; font-size: 20px; }
  .service-item { fill: var(--navy); font-weight: 400; font-size: 19px; }
  .web-address { fill: var(--navy); font-weight: 700; font-size: 26px; }
</style>
</head>
<body>
<main class="canvas">
  <svg class="banner" viewBox="0 0 423 1050" xmlns="http://www.w3.org/2000/svg">
    <defs>
      <linearGradient id="paper" x1="0" y1="0" x2="0" y2="1">
        <stop offset="0" stop-color="var(--paper-top)"/>
        <stop offset="1" stop-color="var(--paper-bottom)"/>
      </linearGradient>
      <linearGradient id="ribbon" x1="0" y1="0" x2="1" y2="0">
        <stop offset="0" stop-color="#3fb0b3"/>
        <stop offset="0.55" stop-color="var(--teal-light)"/>
        <stop offset="1" stop-color="var(--teal-dark)"/>
      </linearGradient>
      <linearGradient id="ideas" x1="0" y1="0" x2="1" y2="0">
        <stop offset="0" stop-color="#d9452c"/>
        <stop offset="0.3" stop-color="#4a62d8"/>
        <stop offset="0.5" stop-color="#f3d12a"/>
        <stop offset="0.72" stop-color="#ee8a26"/>
        <stop offset="1" stop-color="#7cc6e4"/>
      </linearGradient>
      <linearGradient id="pencil" x1="0" y1="0" x2="1" y2="0">
        <stop offset="0" stop-color="var(--teal-dark)"/>
        <stop offset="0.5" stop-color="var(--gold)"/>
        <stop offset="1" stop-color="var(--teal-dark)"/>
      </linearGradient>
    </defs>

    <!-- banner surface -->
    <rect class="banner-surface" width="423" height="1050" fill="url(#paper)"/>

    <!-- header band -->
    <polygon class="header-band" points="0,0 423,0 423,108 211,165 0,108" fill="var(--navy)"/>
    <rect class="idea-bulbs" x="14" y="8" width="395" height="92" rx="14" fill="url(#ideas)" opacity="0.55"
          role="img" aria-label="Row of crumpled-paper light bulbs hanging from the top, one glowing yellow"/>

    <!-- brand -->
    <text class="brand-name" x="211.5" y="258" text-anchor="middle" font-size="74" textLength="300" lengthAdjust="spacingAndGlyphs">PELLACORVA</text>
    <text class="brand-name" x="211.5" y="287" text-anchor="middle" font-size="26" textLength="286" lengthAdjust="spacing">ADVISORY</text>

    <!-- chevron bands -->
    <polygon class="band-left" points="0,288 211,345 211,408 0,355" fill="var(--gold)"/>
    <polygon class="band-right" points="211,345 423,288 423,402 211,408" fill="var(--yellow)"/>

    <!-- head and pencil illustration -->
    <rect class="idea-pencil" x="4" y="305" width="146" height="740" rx="10" fill="url(#pencil)" opacity="0.85"
          role="img" aria-label="Outline of a head shaped like a light bulb resting on a tall yellow pencil with teal tabs"/>

    <!-- service ribbons -->
    <g class="service">
      <polygon points="128,488 412,488 382,545 412,603 128,603" fill="url(#ribbon)"/>
      <text class="service-title" x="142" y="516">EDUCATIONAL CONTENT CREATION</text>
      <text class="service-item" x="142" y="542">• Supplemental Textbook Content</text>
      <text class="service-item" x="152" y="566">Development</text>
      <text class="service-item" x="142" y="591">• E-learning Content Development</text>
    </g>
    <g class="service">
      <polygon points="128,633 412,633 382,675 412,718 128,718" fill="url(#ribbon)"/>
      <text class="service-title" x="142" y="656">CURRICULUM DEVELOPMENT</text>
      <text class="service-item" x="142" y="681">• VKTR/Joint Pillar</text>
      <text class="service-item" x="142" y="706">• Three Dimensional Learning</text>
    </g>
    <g class="service">
      <polygon points="128,739 412,739 382,797 412,855 128,855" fill="url(#ribbon)"/>
      <text class="service-title" x="142" y="765">ASSESSMENT</text>
      <text class="service-item" x="142" y="790">• Formative Assessments</text>
      <text class="service-item" x="142" y="815">• Elementary School, Middle School,</text>
      <text class="service-item" x="152" y="840">High School, College, and Business</text>
    </g>
    <g class="service">
      <polygon points="128,883 412,883 382,925 412,968 128,968" fill="url(#ribbon)"/>
      <text class="service-title" x="142" y="908">PROFESSIONAL DEVELOPMENT</text>
      <text class="service-item" x="142" y="933">• Training</text>
      <text class="service-item" x="142" y="958">• Facilitation</text>
    </g>

    <!-- footer accents -->
    <polygon class="footer-accent" points="380,960 423,925 423,968" fill="var(--yellow)"/>
    <polygon class="footer-accent" points="215,1050 330,1000 423,1050" fill="var(--gold)"/>
    <polygon class="footer-accent" points="330,1000 423,985 423,1050" fill="var(--yellow)"/>

    <text class="web-address" x="126" y="1022">pellacorvaadvisory.com</text>
  </svg>
</main>
</body>
</html>
```